PowerPoint template for Law Firm

We Need a PowerPoint Template for a Law Firm in Switzerland. We are primarly consult in business law. We Need a template for PowerPoint to Show Information to our Clients (inheritence law, corporate law, legal structures etc.) The design should be contemporary, simple and clear. It should be in harmony with our website: www.trovanek.com Style: professional, structured and clearly arranged. Colors: Blue (R: 1, G: 61: B: 105), white. Font: Calibri Ratio: 16: 9 Esamples attached

```html
<!DOCTYPE html>
<html lang="de">
<head>
<meta charset="utf-8">
<title>Trovanek—Lawyers · Präsentationsvorlage</title>
<link href="https://fonts.googleapis.com/css2?family=Carlito:wght@400;700&display=swap" rel="stylesheet">
<style>
:root{
  --navy:#013d69;
  --navy-soft:#2c5d85;
  --stage:#a8a8a8;
  --paper:#ffffff;
  --mist:#ececec;
  --steel:#8a8f95;
  --ink:#222;
  --copy:#555;
}
*{box-sizing:border-box;margin:0;padding:0}
html,body{width:1184px;height:1200px;overflow:hidden}
body{background:var(--stage);font-family:"Carlito",Calibri,sans-serif;position:relative}
.board{position:absolute;left:83px;top:77px;display:grid;grid-template-columns:repeat(4,233px);grid-auto-rows:131px;gap:23px 30px}
.slide{position:relative;width:233px;height:131px;background:var(--paper);overflow:hidden}
.abs{position:absolute}
.title{position:absolute;left:7px;top:7px;padding-left:3px;border-left:1.6px solid var(--navy);font-size:5px;font-weight:700;color:var(--ink);line-height:5px}
.title.caps{text-transform:uppercase}
.title.blue{color:var(--navy)}
.foot{position:absolute;left:6px;right:6px;bottom:3px;border-top:.4px solid #ddd;padding-top:1.5px;font-size:3.2px;font-weight:700;color:var(--navy)}
.copy{font-size:2.6px;line-height:1.4;color:var(--copy)}
.copy.w{color:#e9f0f6}
.label{font-size:3.2px;font-weight:700;color:var(--navy);text-transform:uppercase}
.sub{font-size:2.9px;font-weight:700;color:var(--navy)}
.photo{position:absolute}
.ph-blue{background:linear-gradient(135deg,#1d466d 0%,#5d82a3 45%,#9fb6c9 60%,#21476b 100%)}
.ph-office{background:linear-gradient(125deg,#e8ebee 0%,#aeb9c3 35%,#4d6478 70%,#2a3c4d 100%)}
.ph-grey{background:linear-gradient(160deg,#f1f1f1,#c7cbcf 60%,#9aa1a7)}
.ph-city{background:linear-gradient(175deg,#a9cbe4 0%,#6f93b0 45%,#3f5870 75%,#59785a 100%)}
.ph-warm{background:linear-gradient(135deg,#d8c3ae,#8e786a 45%,#4b5866 80%,#2f3c4a)}
.circ{border-radius:50%;background:var(--navy);color:#fff;display:flex;align-items:center;justify-content:center}
.ic{width:55%;height:55%;fill:currentColor}
.row{display:flex}
</style>
</head>
<body>
<svg width="0" height="0" style="position:absolute">
  <defs>
    <symbol id="i-bank" viewBox="0 0 24 24"><path d="M12 3 2 8h20zM4 10h2v8H4zm5 0h2v8H9zm4 0h2v8h-2zm5 0h2v8h-2zM2 19h20v2H2z"/></symbol>
    <symbol id="i-case" viewBox="0 0 24 24"><path d="M9 4h6v3h5v12H4V7h5zm2 2v1h2V6z"/></symbol>
    <symbol id="i-doc" viewBox="0 0 24 24"><path d="M6 2h8l5 5v15H6zm3 9v1.5h7V11zm0 4v1.5h7V15z"/></symbol>
    <symbol id="i-gear" viewBox="0 0 24 24"><path d="M12 7a5 5 0 1 0 0 10a5 5 0 1 0 0-10zM11 1h2v5h-2zm0 17h2v5h-2zM1 11h5v2H1zm17 0h5v2h-5z"/></symbol>
    <symbol id="i-chat" viewBox="0 0 24 24"><path d="M3 4h18v12H9l-5 4v-4H3z"/></symbol>
    <symbol id="i-home" viewBox="0 0 24 24"><path d="M12 3 2 12h3v9h5v-6h4v6h5v-9h3z"/></symbol>
    <symbol id="i-grid" viewBox="0 0 24 24"><path d="M3 3h8v8H3zm10 0h8v8h-8zM3 13h8v8H3zm10 0h8v8h-8z"/></symbol>
    <symbol id="i-cloud" viewBox="0 0 24 24"><path d="M6 19a4.5 4.5 0 0 1-.5-9A6.5 6.5 0 0 1 18 9a5 5 0 0 1 0 10z"/></symbol>
    <symbol id="i-send" viewBox="0 0 24 24"><path d="M2 11 22 3l-7 18-3-7z"/></symbol>
    <symbol id="i-check" viewBox="0 0 24 24"><path d="M9 16 4 11l-2 2 7 7L22 7l-2-2z"/></symbol>
    <symbol id="i-clock" viewBox="0 0 24 24"><path d="M12 2a10 10 0 1 0 0 20a10 10 0 1 0 0-20zm-1 4h2v6l4 3-1 1.5-5-3.5z"/></symbol>
    <symbol id="i-mail" viewBox="0 0 24 24"><path d="M2 5h20v14H2zm2 2v1l8 5 8-5V7l-8 5z"/></symbol>
  </defs>
</svg>

<main class="board">

  <!-- 1 cover -->
  <section class="slide">
    <div class="photo ph-blue" style="left:0;top:0;width:233px;height:106px" role="img" aria-label="Team meeting in an office, tinted blue"></div>
    <div class="abs" style="left:13px;top:113px;font-size:6.5px;font-weight:700;color:var(--navy)">Trovanek—Lawyers</div>
    <div class="abs" style="right:14px;top:115px;font-size:3.8px;font-weight:700;color:var(--navy)">www.trovanek.com</div>
  </section>

  <!-- 2 intro -->
  <section class="slide">
    <div class="title">Anwaltskanzlei für Wirtschaftsrecht</div>
    <div class="photo ph-office" style="left:96px;top:27px;width:125px;height:82px" role="img" aria-label="Two lawyers meeting at a desk by a window"></div>
    <div class="abs" style="left:13px;top:27px;width:86px;height:85px;background:var(--navy);padding:9px 8px">
      <p style="font-size:3.1px;line-height:1.3;font-weight:700;color:#fff">Ob multinationales Unternehmen, traditionsreiches Familien-KMU, lokaler Gewerbebetrieb, Investmentfund oder Start-up: Trovanek Lawyers begleitet Sie umfassend bei rechtlichen Fragestellungen und steht konsequent für Ihre Anliegen ein. Mit unternehmerischem Verständnis und einer zielorientierten Arbeitsweise ermöglichen wir Ihnen die Fokussierung auf Ihre unternehmerische Kerntätigkeit.</p>
    </div>
    <div class="foot">Trovanek—Lawyers</div>
  </section>

  <!-- 3 areas -->
  <section class="slide">
    <div class="title">Fachgebiet Wirtschaftsrecht:</div>
    <div class="abs" style="left:8px;top:29px;width:101px;text-align:right">
      <div style="height:24px"><div class="sub">Gesellschaftsrecht</div><p class="copy">Gründung, Sitzverlegung, Umstrukturierung, Nachfolgeregelung</p></div>
      <div style="height:24px"><div class="sub">Mergers &amp; Acquisitions</div><p class="copy">Unternehmenskauf, Fusion, Due Diligence, Private Equity</p></div>
      <div style="height:24px"><div class="sub">Handels- und Vertragsrecht</div><p class="copy">Kaufvertrag, Werkvertrag, Auftrag, Vertriebsrecht</p></div>
      <div style="height:24px"><div class="sub">Arbeitsrecht</div><p class="copy">Arbeitsverträge, Kündigung, Mitarbeiterbeteiligung</p></div>
    </div>
    <div class="abs" style="left:112px;top:29px">
      <div class="circ" style="width:13px;height:13px;margin-bottom:11px"><svg class="ic"><use href="#i-bank"/></svg></div>
      <div class="circ" style="width:13px;height:13px;margin-bottom:11px"><svg class="ic"><use href="#i-chat"/></svg></div>
      <div class="circ" style="width:13px;height:13px;margin-bottom:11px"><svg class="ic"><use href="#i-grid"/></svg></div>
      <div class="circ" style="width:13px;height:13px"><svg class="ic"><use href="#i-case"/></svg></div>
    </div>
    <div class="abs" style="left:131px;top:29px">
      <div class="circ" style="width:13px;height:13px;margin-bottom:11px"><svg class="ic"><use href="#i-gear"/></svg></div>
      <div class="circ" style="width:13px;height:13px;margin-bottom:11px"><svg class="ic"><use href="#i-doc"/></svg></div>
      <div class="circ" style="width:13px;height:13px;margin-bottom:11px"><svg class="ic"><use href="#i-send"/></svg></div>
      <div class="circ" style="width:13px;height:13px"><svg class="ic"><use href="#i-home"/></svg></div>
    </div>
    <div class="abs" style="left:148px;top:29px;width:80px">
      <div style="height:24px"><div class="sub">Finanz- und Kapitalmarktrecht</div><p class="copy">Kollektive Anlagen, Private Equity, Compliance</p></div>
      <div style="height:24px"><div class="sub">Wettbewerbs- und Immaterialgüterrecht</div><p class="copy">Marken, Patente, Design, Lizenzen</p></div>
      <div style="height:24px"><div class="sub">Digital Economy, IT-Recht, Datenschutz</div><p class="copy">Softwareverträge, Blockchain, Fintech</p></div>
      <div style="height:24px"><div class="sub">Lorem ipsum dolor</div><p class="copy">Lorem ipsum dolor sit amet, consectetur elit</p></div>
    </div>
    <div class="foot">Trovanek—Lawyers</div>
  </section>

  <!-- 4 three photos -->
  <section class="slide">
    <div class="title caps">Edit title here</div>
    <div class="row abs" style="left:10px;top:23px;gap:4px">
      <div class="ph-warm" style="width:68px;height:54px;border-bottom:1.5px solid var(--navy)" role="img" aria-label="Hands typing on a laptop"></div>
      <div class="ph-grey" style="width:68px;height:54px;border-bottom:1.5px solid var(--navy)" role="img" aria-label="Hand holding a smartphone"></div>
      <div class="ph-city" style="width:68px;height:54px;border-bottom:1.5px solid var(--navy)" role="img" aria-label="Financial chart over a city skyline"></div>
    </div>
    <div class="row abs" style="left:10px;top:82px;gap:4px;text-align:center">
      <div style="width:68px"><div class="label">Lorem ipsum</div><p class="copy">Lorem ipsum dolor sit amet, consectetur adipiscing elit. Curabitur odio ligula, ultrices eu convallis et, condimentum at magna.</p></div>
      <div style="width:68px"><div class="label">Lorem ipsum</div><p class="copy">Lorem ipsum dolor sit amet, consectetur adipiscing elit. Curabitur odio ligula, ultrices eu convallis et, condimentum at magna.</p></div>
      <div style="width:68px"><div class="label">Lorem ipsum</div><p class="copy">Lorem ipsum dolor sit amet, consectetur adipiscing elit. Curabitur odio ligula, ultrices eu convallis et, condimentum at magna.</p></div>
    </div>
    <div class="foot">Trovanek—Lawyers</div>
  </section>

  <!-- 5 team -->
  <section class="slide">
    <div class="title caps">Our team</div>
    <div class="row abs" style="left:16px;top:30px;gap:9px;text-align:center">
      <div style="width:43px"><div class="ph-grey" style="width:34px;height:34px;border-radius:50%;margin:0 auto 4px" role="img" aria-label="Portrait photo"></div><div class="label">Lena Marti</div><div class="copy">General Manager</div></div>
      <div style="width:43px"><div class="ph-warm" style="width:34px;height:34px;border-radius:50%;margin:0 auto 4px" role="img" aria-label="Portrait photo"></div><div class="label">Jonas Keller</div><div class="copy">Trainer Head</div></div>
      <div style="width:43px"><div class="ph-warm" style="width:34px;height:34px;border-radius:50%;margin:0 auto 4px" role="img" aria-label="Portrait photo"></div><div class="label">Noah Frei</div><div class="copy">Finance</div></div>
      <div style="width:43px"><div class="ph-grey" style="width:34px;height:34px;border-radius:50%;margin:0 auto 4px" role="img" aria-label="Portrait photo"></div><div class="label">Elias Brunner</div><div class="copy">Senior Trainer</div></div>
    </div>
    <p class="copy abs" style="left:20px;right:20px;top:88px;text-align:center">Lorem ipsum dolor sit amet, consectetur adipiscing elit, sed do eiusmod tempor incididunt ut labore et dolore magna aliqua. Ut enim ad minim veniam, quis nostrud exercitation ullamco laboris nisi ut aliquip ex ea commodo consequat. Duis aute irure dolor in reprehenderit in voluptate velit esse cillum dolore eu fugiat nulla pariatur. Excepteur sint occaecat cupidatat non proident, sunt in culpa qui officia deserunt mollit anim id est laborum. Sed ut perspiciatis unde omnis iste natus error sit voluptatem.</p>
    <div class="foot">Trovanek—Lawyers</div>
  </section>

  <!-- 6 what sets us apart -->
  <section class="slide">
    <div class="title">Was zeichnet uns aus?</div>
    <div class="photo ph-grey" style="left:11px;top:21px;width:213px;height:64px" role="img" aria-label="Framed chair sketches hanging on a light wall"></div>
    <p class="abs" style="left:14px;right:12px;top:89px;color:#2a2a2a;font-weight:700;font-size:3px;line-height:1.35">Wir begegnen unseren anspruchsvollen Klienten im In- und Ausland mit zielgerichteten Lösungen. Uns zeichnen Flexibilität und kurze Reaktionszeiten aus. Ein hohes Mass an Professionalität und Diskretion ist für uns eine Selbstverständlichkeit. Wir setzen konsequent auf den Einsatz zeitgemässer Technologien und sind mit neuen Medien bestens vertraut. Wir sind Ihr starker Partner in sämtlichen wirtschaftsrechtlichen Belangen und schaffen Vertrauen und Sicherheit.</p>
    <div class="foot">Trovanek—Lawyers</div>
  </section>

  <!-- 7 solutions -->
  <section class="slide">
    <div class="title">In erster Linie zählen Lösungen</div>
    <div class="abs" style="left:0;top:38px;width:233px;height:67px;background:var(--navy)"></div>
    <div class="abs ph-grey" style="left:10px;top:28px;width:62px;height:48px;border-radius:2px" role="img" aria-label="Desktop computer monitor"></div>
    <p class="abs" style="left:86px;top:50px;width:142px;font-size:4px;line-height:1.25;color:#fff">Mit unserem fachlichen Know-how, unserer digitalen Kompetenz und unserer langjährigen Erfahrung erarbeiten wir kreative und verlässliche Lösungen. Kontaktieren Sie uns frühzeitig, um eine bestmögliche Ausgangslage zu schaffen. Bei Bedarf ergänzt ein breites Netzwerk von Spezialisten unsere Kompetenzen.</p>
    <div class="foot">Trovanek—Lawyers</div>
  </section>

  <!-- 8 services -->
  <section class="slide">
    <div class="title caps">Our services</div>
    <div class="abs" style="left:0;top:22px;width:233px;height:95px;background:var(--mist)"></div>
    <div class="abs" style="left:10px;top:30px;display:grid;grid-template-columns:repeat(5,38px);gap:7px 5px;text-align:center;color:var(--navy)">
      <div><svg style="width:8px;height:8px;fill:currentColor"><use href="#i-cloud"/></svg><div class="label" style="font-size:2.8px">Lorem ipsum</div><p class="copy">Lorem ipsum dolor sit amet, consectetur adipiscing elit sed do</p></div>
      <div><svg style="width:8px;height:8px;fill:currentColor"><use href="#i-clock"/></svg><div class="label" style="font-size:2.8px">Lorem ipsum</div><p class="copy">Lorem ipsum dolor sit amet, consectetur adipiscing elit sed do</p></div>
      <div><svg style="width:8px;height:8px;fill:currentColor"><use href="#i-bank"/></svg><div class="label" style="font-size:2.8px">Lorem ipsum</div><p class="copy">Lorem ipsum dolor sit amet, consectetur adipiscing elit sed do</p></div>
      <div><svg style="width:8px;height:8px;fill:currentColor"><use href="#i-chat"/></svg><div class="label" style="font-size:2.8px">Lorem ipsum</div><p class="copy">Lorem ipsum dolor sit amet, consectetur adipiscing elit sed do</p></div>
      <div><svg style="width:8px;height:8px;fill:currentColor"><use href="#i-mail"/></svg><div class="label" style="font-size:2.8px">Lorem ipsum</div><p class="copy">Lorem ipsum dolor sit amet, consectetur adipiscing elit sed do</p></div>
      <div><svg style="width:8px;height:8px;fill:currentColor"><use href="#i-clock"/></svg><div class="label" style="font-size:2.8px">Lorem ipsum</div><p class="copy">Lorem ipsum dolor sit amet, consectetur adipiscing elit sed do</p></div>
      <div><svg style="width:8px;height:8px;fill:currentColor"><use href="#i-gear"/></svg><div class="label" style="font-size:2.8px">Lorem ipsum</div><p class="copy">Lorem ipsum dolor sit amet, consectetur adipiscing elit sed do</p></div>
      <div><svg style="width:8px;height:8px;fill:currentColor"><use href="#i-case"/></svg><div class="label" style="font-size:2.8px">Lorem ipsum</div><p class="copy">Lorem ipsum dolor sit amet, consectetur adipiscing elit sed do</p></div>
      <div><svg style="width:8px;height:8px;fill:currentColor"><use href="#i-doc"/></svg><div class="label" style="font-size:2.8px">Lorem ipsum</div><p class="copy">Lorem ipsum dolor sit amet, consectetur adipiscing elit sed do</p></div>
      <div><svg style="width:8px;height:8px;fill:currentColor"><use href="#i-cloud"/></svg><div class="label" style="font-size:2.8px">Lorem ipsum</div><p class="copy">Lorem ipsum dolor sit amet, consectetur adipiscing elit sed do</p></div>
    </div>
    <div class="foot">Trovanek—Lawyers</div>
  </section>

  <!-- 9 bar chart -->
  <section class="slide">
    <div class="title caps">Edit title here</div>
    <svg class="abs" style="left:10px;top:22px" width="100" height="90" viewBox="0 0 100 90">
      <g stroke="#e3e3e3" stroke-width=".4"><line x1="12" y1="10" x2="96" y2="10"/><line x1="12" y1="25" x2="96" y2="25"/><line x1="12" y1="40" x2="96" y2="40"/><line x1="12" y1="55" x2="96" y2="55"/><line x1="12" y1="70" x2="96" y2="70"/></g>
      <line x1="12" y1="6" x2="12" y2="70" stroke="#999" stroke-width=".5"/>
      <rect x="18" y="62" width="7" height="8" fill="#013d69"/>
      <rect x="30" y="54" width="7" height="16" fill="#8a8f95"/>
      <rect x="42" y="46" width="7" height="24" fill="#013d69"/>
      <rect x="54" y="38" width="7" height="32" fill="#8a8f95"/>
      <rect x="66" y="30" width="7" height="40" fill="#013d69"/>
      <rect x="78" y="18" width="7" height="52" fill="#013d69"/>
      <polyline points="21,62 33,55 45,49 57,40 69,31 81,20 90,9" fill="none" stroke="#333" stroke-width=".6"/>
      <line x1="12" y1="70" x2="96" y2="70" stroke="#999" stroke-width=".5"/>
      <g font-size="2.6" fill="#999"><text x="17" y="75">2013</text><text x="29" y="75">2014</text><text x="41" y="75">2015</text><text x="53" y="75">2016</text><text x="65" y="75">2017</text><text x="77" y="75">2018</text><text x="40" y="81">Lorem ipsum sit</text></g>
      <g font-size="2.4" fill="#888"><circle cx="14" cy="87" r="1.8" fill="#013d69"/><text x="17" y="88">Lorem</text><circle cx="30" cy="87" r="1.8" fill="#8a8f95"/><text x="33" y="88">Lorem</text><circle cx="46" cy="87" r="1.8" fill="#013d69"/><text x="49" y="88">Lorem</text><circle cx="62" cy="87" r="1.8" fill="#8a8f95"/><text x="65" y="88">Lorem</text><circle cx="78" cy="87" r="1.8" fill="#013d69"/><text x="81" y="88">Lorem</text></g>
    </svg>
    <p class="copy abs" style="left:132px;top:20px;width:92px">Lorem ipsum dolor sit amet, consectetur adipiscing elit, sed do eiusmod tempor incididunt ut labore et dolore magna aliqua. Ut enim ad minim veniam, quis nostrud exercitation ullamco laboris nisi ut aliquip ex ea commodo consequat. Duis aute irure dolor in reprehenderit in voluptate velit esse cillum dolore eu fugiat nulla pariatur. Excepteur sint occaecat cupidatat non proident, sunt in culpa qui officia deserunt mollit anim id est laborum. Sed ut perspiciatis unde omnis iste natus error sit voluptatem accusantium doloremque laudantium, totam rem aperiam eaque ipsa quae ab illo inventore veritatis et quasi architecto beatae vitae dicta sunt explicabo. Nemo enim ipsam voluptatem quia voluptas sit aspernatur aut odit aut fugit, sed quia consequuntur magni dolores eos qui ratione voluptatem sequi nesciunt.</p>
    <div class="foot">Trovanek—Lawyers</div>
  </section>

  <!-- 10 text and photo -->
  <section class="slide">
    <div class="title caps">Edit title here</div>
    <div class="photo ph-office" style="left:145px;top:0;width:88px;height:131px" role="img" aria-label="Business people seated in a conference"></div>
    <p class="copy abs" style="left:10px;top:22px;width:128px">Lorem ipsum dolor sit amet, consectetur adipiscing elit, sed do eiusmod tempor incididunt ut labore et dolore magna aliqua. Ut enim ad minim veniam, quis nostrud exercitation ullamco laboris nisi ut aliquip ex ea commodo consequat. Duis aute irure dolor in reprehenderit in voluptate velit esse cillum dolore eu fugiat nulla pariatur. Excepteur sint occaecat cupidatat non proident, sunt in culpa qui officia deserunt mollit anim id est laborum. Sed ut perspiciatis unde omnis iste natus error sit voluptatem accusantium.</p>
    <div class="row abs" style="left:12px;top:78px;gap:6px;text-align:center;color:var(--navy)">
      <div style="width:38px"><svg style="width:10px;height:10px;fill:currentColor"><use href="#i-home"/></svg><p class="copy">Lorem ipsum dolor sit amet, consectetur adipiscing elit sed do</p></div>
      <div style="width:38px"><svg style="width:10px;height:10px;fill:currentColor"><use href="#i-grid"/></svg><p class="copy">Lorem ipsum dolor sit amet, consectetur adipiscing elit sed do</p></div>
      <div style="width:38px"><svg style="width:10px;height:10px;fill:currentColor"><use href="#i-bank"/></svg><p class="copy">Lorem ipsum dolor sit amet, consectetur adipiscing elit sed do</p></div>
    </div>
    <div class="foot" style="right:95px">Trovanek—Lawyers</div>
  </section>

  <!-- 11 blue panel with white box -->
  <section class="slide">
    <div class="title caps">Edit title here</div>
    <div class="photo ph-blue" style="left:0;top:21px;width:233px;height:98px" role="img" aria-label="City skyline at night, tinted blue"></div>
    <div class="abs" style="left:0;top:21px;width:66px;height:98px;background:var(--navy);padding:16px 7px;text-align:center">
      <p style="color:#fff;font-weight:700;font-size:3px;line-height:1.35">Lorem ipsum dolor sit amet consectetur adipiscing elit. Cras bibendum mattis leo, ac efficitur ipsum lobortis non. Praesent vitae pulvinar lorem ipsum dolor sit amet consectetur adipiscing elit. Cras bibendum mattis leo.</p>
    </div>
    <div class="row abs" style="left:83px;top:43px;width:139px;height:52px;background:#fff;justify-content:space-around;align-items:center;color:var(--navy);text-align:center">
      <div><svg style="width:10px;height:10px;fill:currentColor"><use href="#i-grid"/></svg><div class="label">Lorem</div></div>
      <div><svg style="width:10px;height:10px;fill:currentColor"><use href="#i-home"/></svg><div class="label">Lorem</div></div>
      <div><svg style="width:10px;height:10px;fill:currentColor"><use href="#i-gear"/></svg><div class="label">Lorem</div></div>
    </div>
    <div class="foot">Trovanek—Lawyers</div>
  </section>

  <!-- 12 six tabbed boxes -->
  <section class="slide">
    <div class="title caps">Edit title here</div>
    <div class="abs" style="left:30px;top:24px;display:grid;grid-template-columns:repeat(3,52px);gap:9px 7px">
      <div style="position:relative;height:41px;border:.6px solid var(--navy);text-align:center;padding:15px 3px 0"><div class="circ abs" style="left:19px;top:-2px;width:14px;height:13px;border-radius:0 0 3px 3px"><svg class="ic"><use href="#i-gear"/></svg></div><div class="label">Lorem ipsum</div><p class="copy">Lorem ipsum dolor sit amet, consectetur adipiscing elit sed do</p></div>
      <div style="position:relative;height:41px;border:.6px solid var(--navy);text-align:center;padding:15px 3px 0"><div class="circ abs" style="left:19px;top:-2px;width:14px;height:13px;border-radius:0 0 3px 3px"><svg class="ic"><use href="#i-doc"/></svg></div><div class="label">Lorem ipsum</div><p class="copy">Lorem ipsum dolor sit amet, consectetur adipiscing elit sed do</p></div>
      <div style="position:relative;height:41px;border:.6px solid var(--navy);text-align:center;padding:15px 3px 0"><div class="circ abs" style="left:19px;top:-2px;width:14px;height:13px;border-radius:0 0 3px 3px"><svg class="ic"><use href="#i-bank"/></svg></div><div class="label">Lorem ipsum</div><p class="copy">Lorem ipsum dolor sit amet, consectetur adipiscing elit sed do</p></div>
      <div style="position:relative;height:41px;border:.6px solid var(--navy);text-align:center;padding:15px 3px 0"><div class="circ abs" style="left:19px;top:-2px;width:14px;height:13px;border-radius:0 0 3px 3px"><svg class="ic"><use href="#i-chat"/></svg></div><div class="label">Lorem ipsum</div><p class="copy">Lorem ipsum dolor sit amet, consectetur adipiscing elit sed do</p></div>
      <div style="position:relative;height:41px;border:.6px solid var(--navy);text-align:center;padding:15px 3px 0"><div class="circ abs" style="left:19px;top:-2px;width:14px;height:13px;border-radius:0 0 3px 3px"><svg class="ic"><use href="#i-send"/></svg></div><div class="label">Lorem ipsum</div><p class="copy">Lorem ipsum dolor sit amet, consectetur adipiscing elit sed do</p></div>
      <div style="position:relative;height:41px;border:.6px solid var(--navy);text-align:center;padding:15px 3px 0"><div class="circ abs" style="left:19px;top:-2px;width:14px;height:13px;border-radius:0 0 3px 3px"><svg class="ic"><use href="#i-check"/></svg></div><div class="label">Lorem ipsum</div><p class="copy">Lorem ipsum dolor sit amet, consectetur adipiscing elit sed do</p></div>
    </div>
    <div class="foot">Trovanek—Lawyers</div>
  </section>

  <!-- 13 icon list and photo -->
  <section class="slide">
    <div class="title caps">Edit title here</div>
    <div class="photo ph-office" style="left:110px;top:0;width:123px;height:131px" role="img" aria-label="Hands reviewing documents with a tablet"></div>
    <div class="abs" style="left:20px;top:27px">
      <div class="row" style="gap:5px;height:24px"><div class="circ" style="width:12px;height:12px;flex:none"><svg class="ic"><use href="#i-bank"/></svg></div><div><div class="sub">Lorem ipsum dolor</div><p class="copy" style="width:64px">Lorem ipsum dolor sit amet, consectetur adipiscing elit, sed do eiusmod tempor</p></div></div>
      <div class="row" style="gap:5px;height:24px"><div class="circ" style="width:12px;height:12px;flex:none"><svg class="ic"><use href="#i-chat"/></svg></div><div><div class="sub">Lorem ipsum dolor</div><p class="copy" style="width:64px">Lorem ipsum dolor sit amet, consectetur adipiscing elit, sed do eiusmod tempor</p></div></div>
      <div class="row" style="gap:5px;height:24px"><div class="circ" style="width:12px;height:12px;flex:none"><svg class="ic"><use href="#i-grid"/></svg></div><div><div class="sub">Lorem ipsum dolor</div><p class="copy" style="width:64px">Lorem ipsum dolor sit amet, consectetur adipiscing elit, sed do eiusmod tempor</p></div></div>
      <div class="row" style="gap:5px;height:24px"><div class="circ" style="width:12px;height:12px;flex:none"><svg class="ic"><use href="#i-case"/></svg></div><div><div class="sub">Lorem ipsum dolor</div><p class="copy" style="width:64px">Lorem ipsum dolor sit amet, consectetur adipiscing elit, sed do eiusmod tempor</p></div></div>
    </div>
    <div class="foot" style="right:128px">Trovanek—Lawyers</div>
  </section>

  <!-- 14 section title -->
  <section class="slide">
    <div class="photo ph-blue" style="left:0;top:0;width:233px;height:131px" role="img" aria-label="Stacked coins with financial data overlay"></div>
    <div class="abs" style="left:16px;top:0;width:80px;height:131px;background:rgba(1,61,105,.92);padding:37px 8px;text-align:center;color:#fff">
      <div style="font-size:7.8px;font-weight:700;border-bottom:.5px solid #fff;padding-bottom:2px;margin-bottom:4px">Section Title</div>
      <p style="font-size:3.4px;line-height:1.3;color:#e9f0f6">Lorem ipsum dolor sit amet, consectetur adipiscing elit. Curabitur odio ligula, ultrices eu convallis et, condimentum at magna. Sed finibus, felis ullamcorper interdum ullamcorper, libero ex</p>
    </div>
  </section>

  <!-- 15 text and network illustration -->
  <section class="slide">
    <div class="title caps">Edit title here</div>
    <p class="copy abs" style="left:10px;top:22px;width:110px">Lorem ipsum dolor sit amet, consectetur adipiscing elit, sed do eiusmod tempor incididunt ut labore et dolore magna aliqua. Ut enim ad minim veniam, quis nostrud exercitation ullamco laboris nisi ut aliquip ex ea commodo consequat. Duis aute irure dolor in reprehenderit in voluptate velit esse cillum dolore eu fugiat nulla pariatur. Excepteur sint occaecat cupidatat non proident, sunt in culpa qui officia deserunt mollit anim id est laborum.<br><br>Sed ut perspiciatis unde omnis iste natus error sit voluptatem accusantium doloremque laudantium, totam rem aperiam, eaque ipsa quae ab illo inventore veritatis et quasi architecto beatae vitae dicta sunt explicabo. Nemo enim ipsam voluptatem quia voluptas sit aspernatur aut odit aut fugit, sed quia consequuntur magni dolores eos qui ratione voluptatem sequi nesciunt.</p>
    <div class="photo" style="left:126px;top:20px;width:98px;height:98px;border-radius:50%;background:radial-gradient(circle at 50% 45%,#4d7aa2 0%,#1f5683 35%,rgba(1,61,105,.35) 60%,rgba(255,255,255,0) 72%)" role="img" aria-label="Illustration of a tree of connected service icons in blue circles"></div>
    <div class="foot">Trovanek—Lawyers</div>
  </section>

  <!-- 16 photo and navy list -->
  <section class="slide">
    <div class="title caps">Edit title here</div>
    <div class="photo ph-warm" style="left:0;top:24px;width:116px;height:88px" role="img" aria-label="Colleagues working together at a laptop"></div>
    <div class="abs" style="left:116px;top:26px;width:117px;height:86px;background:var(--navy);padding:8px 8px;color:#fff">
      <div class="row" style="gap:6px;height:25px"><svg style="width:9px;height:9px;fill:#fff;flex:none"><use href="#i-cloud"/></svg><div><div class="label" style="color:#fff;font-size:2.8px">Lorem ipsum</div><p class="copy w">Lorem ipsum dolor sit amet, consectetur adipiscing elit, sed do eiusmod tempor incididunt ut labore</p></div></div>
      <div class="row" style="gap:6px;height:25px"><svg style="width:9px;height:9px;fill:#fff;flex:none"><use href="#i-clock"/></svg><div><div class="label" style="color:#fff;font-size:2.8px">Lorem ipsum</div><p class="copy w">Lorem ipsum dolor sit amet, consectetur adipiscing elit, sed do eiusmod tempor incididunt ut labore</p></div></div>
      <div class="row" style="gap:6px;height:25px"><svg style="width:9px;height:9px;fill:#fff;flex:none"><use href="#i-bank"/></svg><div><div class="label" style="color:#fff;font-size:2.8px">Lorem ipsum</div><p class="copy w">Lorem ipsum dolor sit amet, consectetur adipiscing elit, sed do eiusmod tempor incididunt ut labore</p></div></div>
    </div>
    <div class="foot">Trovanek—Lawyers</div>
  </section>

  <!-- 17 icon cards -->
  <section class="slide">
    <div class="title caps">Edit title here</div>
    <div class="abs" style="left:0;top:22px;width:233px;height:100px;background:var(--mist)"></div>
    <div class="abs" style="left:19px;top:27px;display:grid;grid-template-columns:repeat(3,59px);gap:6px 10px">
      <div style="height:40px;background:#fff;border:.6px solid var(--navy);position:relative;color:var(--navy);text-align:center;padding-top:8px"><svg style="width:14px;height:14px;fill:currentColor"><use href="#i-case"/></svg><div class="abs" style="left:2px;right:2px;bottom:2px;background:var(--navy);color:#fff;font-size:2.6px;font-weight:700;padding:1.5px 0">LOREM IPSUM DOLOR</div></div>
      <div style="height:40px;background:#fff;border:.6px solid var(--navy);position:relative;color:var(--navy);text-align:center;padding-top:8px"><svg style="width:14px;height:14px;fill:currentColor"><use href="#i-chat"/></svg><div class="abs" style="left:2px;right:2px;bottom:2px;background:var(--navy);color:#fff;font-size:2.6px;font-weight:700;padding:1.5px 0">LOREM IPSUM DOLOR</div></div>
      <div style="height:40px;background:#fff;border:.6px solid var(--navy);position:relative;color:var(--navy);text-align:center;padding-top:8px"><svg style="width:14px;height:14px;fill:currentColor"><use href="#i-gear"/></svg><div class="abs" style="left:2px;right:2px;bottom:2px;background:var(--navy);color:#fff;font-size:2.6px;font-weight:700;padding:1.5px 0">LOREM IPSUM DOLOR</div></div>
      <div style="height:40px;background:#fff;border:.6px solid var(--navy);position:relative;color:var(--navy);text-align:center;padding-top:8px"><svg style="width:14px;height:14px;fill:currentColor"><use href="#i-case"/></svg><div class="abs" style="left:2px;right:2px;bottom:2px;background:var(--navy);color:#fff;font-size:2.6px;font-weight:700;padding:1.5px 0">LOREM IPSUM DOLOR</div></div>
      <div style="height:40px;background:#fff;border:.6px solid var(--navy);position:relative;color:var(--navy);text-align:center;padding-top:8px"><svg style="width:14px;height:14px;fill:currentColor"><use href="#i-grid"/></svg><div class="abs" style="left:2px;right:2px;bottom:2px;background:var(--navy);color:#fff;font-size:2.6px;font-weight:700;padding:1.5px 0">LOREM IPSUM DOLOR</div></div>
      <div style="height:40px;background:#fff;border:.6px solid var(--navy);position:relative;color:var(--navy);text-align:center;padding-top:8px"><svg style="width:14px;height:14px;fill:currentColor"><use href="#i-doc"/></svg><div class="abs" style="left:2px;right:2px;bottom:2px;background:var(--navy);color:#fff;font-size:2.6px;font-weight:700;padding:1.5px 0">LOREM IPSUM DOLOR</div></div>
    </div>
    <div class="foot">Trovanek—Lawyers</div>
  </section>

  <!-- 18 table -->
  <section class="slide">
    <div class="title caps">Edit title here</div>
    <table class="abs" style="left:16px;top:35px;width:203px;border-collapse:collapse;font-size:3.2px;text-align:center">
      <tr style="background:var(--navy);color:#fff;font-weight:700;height:10px"><td>Lorem</td><td>Lorem</td><td>Lorem</td><td>Lorem</td></tr>
      <tr style="background:#d9dadc;color:#555;height:9px"><td>Lorem</td><td>Lorem</td><td>Lorem</td><td>Lorem</td></tr>
      <tr style="background:#f1f1f2;color:#555;height:9px"><td>Lorem</td><td>Lorem</td><td>Lorem</td><td>Lorem</td></tr>
      <tr style="background:#d9dadc;color:#555;height:9px"><td>Lorem</td><td>Lorem</td><td>Lorem</td><td>Lorem</td></tr>
      <tr style="background:#f1f1f2;color:#555;height:9px"><td>Lorem</td><td>Lorem</td><td>Lorem</td><td>Lorem</td></tr>
      <tr style="background:#d9dadc;color:#555;height:9px"><td>Lorem</td><td>Lorem</td><td>Lorem</td><td>Lorem</td></tr>
    </table>
    <div class="foot">Trovanek—Lawyers</div>
  </section>

  <!-- 19 two navy text boxes -->
  <section class="slide">
    <div class="title caps">Edit title here</div>
    <div class="abs" style="left:0;top:22px;width:233px;height:96px;background:var(--mist)"></div>
    <div class="photo" style="left:120px;top:22px;width:113px;height:96px;background:linear-gradient(160deg,#e0e5e9,#8393a0 60%,#4d5d6b)" role="img" aria-label="Close-up of a laptop keyboard"></div>
    <p class="copy abs" style="left:8px;top:28px;width:64px;text-align:center">Lorem ipsum dolor sit amet, consectetur adipiscing elit. Donec laoreet, sem at rutrum porta, nisi sem molestie felis, ut porttitor est magna nec nibh. Curabitur eu purus vel ante euismod facilisis. Sed dictum, turpis at ultricies rutrum, lectus sapien cursus est, vitae suscipit odio justo eget sem. Vestibulum enim enim, ultricies quis placerat sed, aliquam eu ipsum.</p>
    <div class="row abs" style="left:74px;top:30px;gap:3px">
      <div style="width:66px;height:82px;background:var(--navy);padding:3px 4px;text-align:center"><div style="font-size:3.4px;font-weight:700;color:#fff;margin-bottom:1px">Lorem ipsum</div><p style="font-size:2.6px;line-height:1.4;color:#e9f0f6;font-weight:700">Lorem ipsum dolor sit amet, consectetur adipiscing elit. Donec laoreet, sem at rutrum porta, nisi sem molestie felis, ut porttitor est magna nec nibh. Curabitur eu purus vel ante euismod facilisis. Sed dictum, turpis at ultricies rutrum, lectus sapien cursus est, vitae suscipit odio justo eget sem.</p></div>
      <div style="width:66px;height:82px;background:var(--navy);padding:3px 4px;text-align:center"><div style="font-size:3.4px;font-weight:700;color:#fff;margin-bottom:1px">Lorem ipsum</div><p style="font-size:2.6px;line-height:1.4;color:#e9f0f6;font-weight:700">Lorem ipsum dolor sit amet, consectetur adipiscing elit. Donec laoreet, sem at rutrum porta, nisi sem molestie felis, ut porttitor est magna nec nibh. Curabitur eu purus vel ante euismod facilisis. Sed dictum, turpis at ultricies rutrum, lectus sapien cursus est, vitae suscipit odio justo eget sem.</p></div>
    </div>
    <div class="foot">Trovanek—Lawyers</div>
  </section>

  <!-- 20 blocks -->
  <section class="slide">
    <div class="title caps">Edit title here</div>
    <p class="copy abs" style="left:10px;top:22px;width:100px">Lorem ipsum dolor sit amet, consectetur adipiscing elit, sed do eiusmod tempor incididunt ut labore et dolore magna aliqua. Ut enim ad minim veniam, quis nostrud exercitation ullamco laboris nisi ut aliquip ex ea commodo consequat. Duis aute irure dolor in reprehenderit in voluptate velit esse cillum dolore eu fugiat nulla pariatur. Excepteur sint occaecat cupidatat non proident, sunt in culpa qui officia deserunt mollit anim id est laborum. Sed ut perspiciatis unde omnis iste natus error sit voluptatem accusantium doloremque laudantium, totam rem aperiam eaque ipsa quae ab illo inventore veritatis et quasi architecto beatae vitae dicta sunt explicabo.</p>
    <div class="abs" style="left:118px;top:26px;display:grid;grid-template-columns:repeat(4,24px);gap:1px;font-size:2.8px;color:#fff;text-align:center">
      <div style="height:24px;background:var(--steel);padding-top:9px">Lorem</div>
      <div style="height:24px;background:var(--navy);padding-top:9px">Lorem</div>
      <div style="height:24px;background:var(--steel);padding-top:9px">Lorem</div>
      <div style="height:24px;background:var(--navy);padding-top:9px">Lorem</div>
      <div style="height:24px;background:var(--navy);padding-top:9px">Lorem</div>
      <div style="height:24px;background:var(--steel);padding-top:9px">Lorem</div>
      <div style="height:24px;background:var(--navy);padding-top:9px">Lorem</div>
      <div style="height:24px;background:#fff"></div>
      <div style="height:24px;background:#fff"></div>
      <div style="height:24px;background:var(--navy);padding-top:9px">Lorem</div>
      <div style="height:24px;background:var(--steel);padding-top:9px">Lorem</div>
      <div style="height:24px;background:var(--navy);padding-top:9px">Lorem</div>
    </div>
    <div class="row abs" style="left:122px;top:111px;gap:10px;font-size:2.4px;color:#888;align-items:center">
      <span><span style="display:inline-block;width:4px;height:4px;border-radius:50%;background:var(--navy)"></span> Lorem</span>
      <span><span style="display:inline-block;width:4px;height:4px;border-radius:50%;background:var(--steel)"></span> Lorem</span>
      <span><span style="display:inline-block;width:4px;height:4px;border-radius:50%;background:var(--navy)"></span> Lorem</span>
      <span><span style="display:inline-block;width:4px;height:4px;border-radius:50%;background:var(--steel)"></span> Lorem</span>
    </div>
    <div class="foot">Trovanek—Lawyers</div>
  </section>

  <!-- 21 area chart -->
  <section class="slide">
    <div class="title caps">Edit title here</div>
    <svg class="abs" style="left:8px;top:22px" width="150" height="95" viewBox="0 0 150 95">
      <g stroke="#e5e5e5" stroke-width=".4"><line x1="8" y1="10" x2="148" y2="10"/><line x1="8" y1="25" x2="148" y2="25"/><line x1="8" y1="40" x2="148" y2="40"/><line x1="8" y1="55" x2="148" y2="55"/><line x1="8" y1="70" x2="148" y2="70"/></g>
      <polygon points="8,70 8,45 40,22 75,30 110,18 148,22 148,70" fill="#b9bcc0"/>
      <polygon points="8,70 8,55 40,40 75,48 110,40 148,30 148,70" fill="#6d99c2"/>
      <polygon points="8,70 8,62 40,54 75,56 110,52 148,48 148,70" fill="#013d69"/>
      <g fill="#2a6aa0"><rect x="34" y="14" width="16" height="4"/><rect x="104" y="12" width="16" height="4"/><rect x="134" y="26" width="14" height="4"/><rect x="34" y="44" width="16" height="4"/><rect x="68" y="42" width="16" height="4"/></g>
      <g font-size="2.2" fill="#fff"><text x="35.5" y="17">Critical Value</text><text x="105.5" y="15">Critical Value</text><text x="135" y="29">Critical</text><text x="35.5" y="47">Critical Value</text><text x="69.5" y="45">Critical Value</text></g>
      <g font-size="2.4" fill="#999"><text x="8" y="75">Item 1</text><text x="40" y="75">Item 2</text><text x="75" y="75">Item 3</text><text x="110" y="75">Item 4</text><text x="140" y="75">Item 5</text></g>
      <g font-size="2.4" fill="#999"><circle cx="26" cy="86" r="1.6" fill="#013d69"/><text x="28" y="87">Lorem ipsum</text><circle cx="48" cy="86" r="1.6" fill="#6d99c2"/><text x="50" y="87">Lorem ipsum</text><circle cx="70" cy="86" r="1.6" fill="#b9bcc0"/><text x="72" y="87">Lorem ipsum</text><circle cx="92" cy="86" r="1.6" fill="#013d69"/><text x="94" y="87">Lorem ipsum</text><circle cx="114" cy="86" r="1.6" fill="#6d99c2"/><text x="116" y="87">Lorem ipsum</text></g>
    </svg>
    <div class="abs" style="left:167px;top:20px;width:66px;height:100px;background:var(--mist);padding:6px 5px">
      <p class="copy">Lorem ipsum dolor sit amet, consectetur adipiscing elit, sed do eiusmod tempor incididunt ut labore et dolore magna aliqua. Ut enim ad minim veniam, quis nostrud exercitation ullamco laboris nisi ut aliquip ex ea commodo consequat. Duis aute irure dolor in reprehenderit in voluptate velit esse cillum dolore eu fugiat nulla pariatur. Excepteur sint occaecat cupidatat non proident, sunt in culpa qui officia deserunt mollit anim id est laborum.</p>
    </div>
    <div class="foot" style="right:70px">Trovanek—Lawyers</div>
  </section>

  <!-- 22 navy box and meeting photo -->
  <section class="slide">
    <div class="title caps blue">Edit title here</div>
    <div class="photo ph-office" style="left:105px;top:26px;width:123px;height:88px" role="img" aria-label="Meeting room with people around a long table"></div>
    <div class="abs" style="left:0;top:26px;width:105px;height:88px;background:var(--navy);padding:11px 14px">
      <div style="font-size:5px;font-weight:700;color:#fff;margin-bottom:3px">LOREM IPSUM</div>
      <p class="copy w">Lorem ipsum dolor sit amet, consectetur adipiscing elit, sed do eiusmod tempor incididunt ut labore et dolore magna aliqua. Ut enim ad minim veniam, quis nostrud exercitation ullamco laboris nisi ut aliquip ex ea commodo consequat. Duis aute irure dolor in reprehenderit in voluptate velit esse cillum dolore eu fugiat nulla pariatur. Excepteur sint occaecat cupidatat non proident, sunt in culpa qui officia deserunt mollit anim id est laborum. Sed ut perspiciatis unde omnis iste natus error.</p>
    </div>
    <div class="foot">Trovanek—Lawyers</div>
  </section>

  <!-- 23 numbered list and building -->
  <section class="slide">
    <div class="title caps blue">Edit title here</div>
    <div class="abs" style="left:0;top:24px;width:233px;height:92px;background:#f3f3f3"></div>
    <div class="photo ph-city" style="left:140px;top:22px;width:84px;height:92px" role="img" aria-label="Modern glass office building"></div>
    <ol class="abs" style="left:16px;top:28px;list-style:none;font-size:2.9px;color:#444">
      <li class="row" style="gap:6px;align-items:center;height:13.5px"><span style="width:6px;height:6px;background:var(--navy);color:#fff;font-weight:700;text-align:center;line-height:6px">1</span>Lorem ipsum dolor sit amet, consectetur adipiscing elit</li>
      <li class="row" style="gap:6px;align-items:center;height:13.5px"><span style="width:6px;height:6px;background:var(--navy);color:#fff;font-weight:700;text-align:center;line-height:6px">2</span>Lorem ipsum dolor sit amet, consectetur adipiscing elit</li>
      <li class="row" style="gap:6px;align-items:center;height:13.5px"><span style="width:6px;height:6px;background:var(--navy);color:#fff;font-weight:700;text-align:center;line-height:6px">3</span>Lorem ipsum dolor sit amet, consectetur adipiscing elit</li>
      <li class="row" style="gap:6px;align-items:center;height:13.5px"><span style="width:6px;height:6px;background:var(--navy);color:#fff;font-weight:700;text-align:center;line-height:6px">4</span>Lorem ipsum dolor sit amet, consectetur adipiscing elit</li>
      <li class="row" style="gap:6px;align-items:center;height:13.5px"><span style="width:6px;height:6px;background:var(--navy);color:#fff;font-weight:700;text-align:center;line-height:6px">5</span>Lorem ipsum dolor sit amet, consectetur adipiscing elit</li>
      <li class="row" style="gap:6px;align-items:center;height:13.5px"><span style="width:6px;height:6px;background:var(--navy);color:#fff;font-weight:700;text-align:center;line-height:6px">6</span>Lorem ipsum dolor sit amet, consectetur adipiscing elit</li>
    </ol>
    <div class="foot">Trovanek—Lawyers</div>
  </section>

  <!-- 24 six columns -->
  <section class="slide">
    <div class="title caps">Edit title here</div>
    <div class="row abs" style="left:14px;top:32px;gap:3px">
      <div style="width:32px"><div class="ph-office" style="height:32px" role="img" aria-label="Business professional"></div><div style="height:42px;background:#2f3a46;padding:3px"><div style="font-size:2.6px;font-weight:700;color:#fff;text-align:center;border-bottom:.4px solid #fff;margin-bottom:1px">TITLE HERE</div><p style="font-size:2.2px;line-height:1.4;color:#e9f0f6">Lorem ipsum dolor sit amet lorem ipsum dolor sit amet lorem ipsum dolor</p></div></div>
      <div style="width:32px"><div class="ph-warm" style="height:32px" role="img" aria-label="Clock detail"></div><div style="height:42px;background:#2f3a46;padding:3px"><div style="font-size:2.6px;font-weight:700;color:#fff;text-align:center;border-bottom:.4px solid #fff;margin-bottom:1px">TITLE HERE</div><p style="font-size:2.2px;line-height:1.4;color:#e9f0f6">Lorem ipsum dolor sit amet lorem ipsum dolor sit amet lorem ipsum dolor</p></div></div>
      <div style="width:32px"><div class="ph-blue" style="height:32px" role="img" aria-label="Team at a desk"></div><div style="height:42px;background:#2f3a46;padding:3px"><div style="font-size:2.6px;font-weight:700;color:#fff;text-align:center;border-bottom:.4px solid #fff;margin-bottom:1px">TITLE HERE</div><p style="font-size:2.2px;line-height:1.4;color:#e9f0f6">Lorem ipsum dolor sit amet lorem ipsum dolor sit amet lorem ipsum dolor</p></div></div>
      <div style="width:32px"><div class="ph-grey" style="height:32px" role="img" aria-label="Person on the phone"></div><div style="height:42px;background:#2f3a46;padding:3px"><div style="font-size:2.6px;font-weight:700;color:#fff;text-align:center;border-bottom:.4px solid #fff;margin-bottom:1px">TITLE HERE</div><p style="font-size:2.2px;line-height:1.4;color:#e9f0f6">Lorem ipsum dolor sit amet lorem ipsum dolor sit amet lorem ipsum dolor</p></div></div>
      <div style="width:32px"><div class="ph-city" style="height:32px" role="img" aria-label="Office workspace"></div><div style="height:42px;background:#2f3a46;padding:3px"><div style="font-size:2.6px;font-weight:700;color:#fff;text-align:center;border-bottom:.4px solid #fff;margin-bottom:1px">TITLE HERE</div><p style="font-size:2.2px;line-height:1.4;color:#e9f0f6">Lorem ipsum dolor sit amet lorem ipsum dolor sit amet lorem ipsum dolor</p></div></div>
      <div style="width:32px"><div class="ph-office" style="height:32px" role="img" aria-label="Laptop on a desk"></div><div style="height:42px;background:#2f3a46;padding:3px"><div style="font-size:2.6px;font-weight:700;color:#fff;text-align:center;border-bottom:.4px solid #fff;margin-bottom:1px">TITLE HERE</div><p style="font-size:2.2px;line-height:1.4;color:#e9f0f6">Lorem ipsum dolor sit amet lorem ipsum dolor sit amet lorem ipsum dolor</p></div></div>
    </div>
    <div class="foot">Trovanek—Lawyers</div>
  </section>

  <!-- 25 map -->
  <section class="slide">
    <div class="title caps blue">Edit title here</div>
    <div class="photo" style="left:62px;top:26px;width:110px;height:86px;background:radial-gradient(ellipse at center,#d6d6d6,#eeeeee 60%,#fafafa 80%)" role="img" aria-label="World map in light grey"></div>
    <svg class="abs" style="left:0;top:0" width="233" height="131" viewBox="0 0 233 131">
      <path d="M56 32 Q110 20 160 40 M110 55 Q80 70 70 82 M110 55 Q150 70 160 85 M56 32 Q90 45 110 55" fill="none" stroke="#999" stroke-width=".5"/>
    </svg>
    <div class="circ abs" style="left:52px;top:28px;width:9px;height:9px"><svg class="ic"><use href="#i-case"/></svg></div>
    <div class="circ abs" style="left:156px;top:36px;width:9px;height:9px"><svg class="ic"><use href="#i-chat"/></svg></div>
    <div class="circ abs" style="left:104px;top:50px;width:11px;height:11px;background:var(--steel)"><svg class="ic"><use href="#i-cloud"/></svg></div>
    <div class="circ abs" style="left:66px;top:78px;width:9px;height:9px"><svg class="ic"><use href="#i-bank"/></svg></div>
    <div class="circ abs" style="left:156px;top:82px;width:9px;height:9px"><svg class="ic"><use href="#i-doc"/></svg></div>
    <div class="abs" style="left:14px;top:34px;width:36px"><div style="font-size:2.9px;font-weight:700">Lorem ipsum</div><p class="copy">Lorem ipsum dolor sit amet, consectetur adipiscing elit. Phasellus sodales, ligula ultrices tempus tristique.</p></div>
    <div class="abs" style="left:184px;top:34px;width:38px"><div style="font-size:2.9px;font-weight:700">Lorem ipsum</div><p class="copy">Lorem ipsum dolor sit amet, consectetur adipiscing elit. Phasellus sodales, ligula ultrices.</p></div>
    <div class="abs" style="left:100px;top:64px;width:36px"><div style="font-size:2.9px;font-weight:700">Lorem ipsum</div><p class="copy">Lorem ipsum dolor sit amet, consectetur adipiscing elit. Phasellus sodales, ligula ultrices.</p></div>
    <div class="abs" style="left:184px;top:78px;width:38px"><div style="font-size:2.9px;font-weight:700">Lorem ipsum</div><p class="copy">Lorem ipsum dolor sit amet, consectetur adipiscing elit. Phasellus sodales.</p></div>
    <div class="foot">Trovanek—Lawyers</div>
  </section>

  <!-- 26 four round icons -->
  <section class="slide">
    <div class="title caps blue">Edit title here</div>
    <div class="abs" style="left:0;top:26px;width:233px;height:88px;background:var(--mist)"></div>
    <div class="row abs" style="left:20px;top:37px;gap:12px;text-align:center">
      <div style="width:40px"><div class="circ" style="width:32px;height:32px;margin:0 auto 4px;border:1.5px solid #fff;box-shadow:0 0 0 .6px var(--navy)"><svg class="ic"><use href="#i-home"/></svg></div><div class="sub">Lorem ipsum dolor</div><p class="copy">Lorem ipsum dolor sit amet, consectetur adipiscing elit. Mauris porttitor lectus ac sapien</p></div>
      <div style="width:40px"><div class="circ" style="width:32px;height:32px;margin:0 auto 4px;border:1.5px solid #fff;box-shadow:0 0 0 .6px var(--navy)"><svg class="ic"><use href="#i-grid"/></svg></div><div class="sub">Lorem ipsum dolor</div><p class="copy">Lorem ipsum dolor sit amet, consectetur adipiscing elit. Mauris porttitor lectus ac sapien</p></div>
      <div style="width:40px"><div class="circ" style="width:32px;height:32px;margin:0 auto 4px;border:1.5px solid #fff;box-shadow:0 0 0 .6px var(--navy)"><svg class="ic"><use href="#i-bank"/></svg></div><div class="sub">Lorem ipsum dolor</div><p class="copy">Lorem ipsum dolor sit amet, consectetur adipiscing elit. Mauris porttitor lectus ac sapien</p></div>
      <div style="width:40px"><div class="circ" style="width:32px;height:32px;margin:0 auto 4px;border:1.5px solid #fff;box-shadow:0 0 0 .6px var(--navy)"><svg class="ic"><use href="#i-send"/></svg></div><div class="sub">Lorem ipsum dolor</div><p class="copy">Lorem ipsum dolor sit amet, consectetur adipiscing elit. Mauris porttitor lectus ac sapien</p></div>
    </div>
    <div class="foot">Trovanek—Lawyers</div>
  </section>

  <!-- 27 quote -->
  <section class="slide" style="background:#e4e4e4">
    <div class="abs" style="left:0;top:0;width:233px;height:64px;background:var(--navy)"></div>
    <div class="abs" style="left:10px;top:2px;font-size:14px;font-weight:700;color:#fff">“</div>
    <div class="abs" style="right:10px;top:44px;font-size:14px;font-weight:700;color:#fff">”</div>
    <p class="abs" style="left:24px;right:24px;top:17px;font-size:4.4px;line-height:1.3;font-weight:700;color:#fff;text-align:center">“Lorem ipsum dolor sit amet, consectetur adipiscing elit. Phasellus sodales, ligula ultrices tempus tristique, tellus justo aliquam dui, nec Lorem ipsum dolor sit amet, consectetur adipiscing elit. elit. Lorem ipsum dolor sit amet, consectetur sit amet, consectetur adipiscing”</p>
    <div class="ph-warm abs" style="left:98px;top:53px;width:37px;height:37px;border-radius:50%;border:1.5px solid #fff" role="img" aria-label="Portrait photo"></div>
    <div class="abs" style="left:0;right:0;top:95px;text-align:center;font-size:4.8px;color:#555">Name Surname</div>
    <div class="abs" style="left:0;right:0;top:102px;text-align:center;font-size:2.8px;color:#999">Chief Operating Officer</div>
  </section>

  <!-- 28 thank you -->
  <section class="slide" style="background:var(--navy)">
    <div class="abs" style="left:0;top:0;width:233px;height:131px;background:linear-gradient(120deg,rgba(255,255,255,.07),rgba(255,255,255,0) 60%)"></div>
    <div class="abs" style="left:66px;top:17px;width:101px;height:24px;border-top:.5px solid #fff;border-bottom:.5px solid #fff;text-align:center;font-size:14px;line-height:23px;color:#fff;letter-spacing:.3px">THANK YOU</div>
    <div class="abs" style="left:30px;top:58px;width:82px;color:#fff">
      <div style="font-size:4px;font-weight:700;margin-bottom:3px">Get in touch to find out more</div>
      <p style="font-size:2.6px;line-height:1.4;color:#e9f0f6;font-weight:700">Book a non-binding initial consultation with us. We would be happy to advise you in a one-to-one basis and give you an estimate and transparent breakdown of our costs.<br><br>To ensure we have enough time to discuss your issues, we kindly ask that you arrange a prior appointment during our office hours, between 7.30 a.m. and 6.00 p.m.</p>
    </div>
    <div class="abs" style="left:128px;top:58px;width:85px;color:#fff">
      <div style="font-size:4.4px;font-weight:700;margin-bottom:3px">Trovanek Lawyers AG</div>
      <p style="font-size:2.6px;line-height:1.4;color:#e9f0f6;font-weight:700">Seestrasse 42 – CH-9000 Lindenau<br>+41 00 000 00 00 – contact@trovanek.com<br><br>Lindenau · Seeberg · Talheim<br><br>www.trovanek.com</p>
    </div>
  </section>

</main>
</body>
</html>
```